Business Card crystal logo Design

crystal store and healing centre ,

view our website to get an idea wildmossgems.com.au
i like our picture of the crystal that on our window display on our store , we also have the words (experience peace & serenity ) just under the name wildmoss gems '
The back of the card ; we definitely need a new logo design
With special: receive 9 treatments from our qualified Practioners
And receive a bonus 50%off over $250 crystals,gems ,minerals
Conditions apply

Industry/Entity Type

Store

Contact Information for Business Card

Wildmoss Gems Pty Ltd
director marla kovenberg
address 482 linden road glen iris victoria 3146
1300519 362

```html
<!DOCTYPE html>
<html lang="en">
<head>
<meta charset="utf-8">
<title>Wildmoss Gems — Business Card</title>
<link rel="stylesheet" href="https://fonts.googleapis.com/css2?family=Josefin+Sans:wght@400;600&family=Questrial&display=swap">
<style>
  :root {
    --page: #f4f3f5;
    --violet-deep: #5e2591;
    --violet: #7a3bb0;
    --violet-light: #8f55c2;
    --lavender: #c9b8e0;
    --lavender-pale: #e7def1;
    --ink-violet: #5a2f86;
    --band: #3a3a3c;
    --rule: #e9e9ec;
    --white: #ffffff;
    --text-dark: #3f3550;
  }
  * { box-sizing: border-box; margin: 0; padding: 0; }
  html, body {
    width: 1200px;
    height: 798px;
    overflow: hidden;
    background: var(--page);
  }
  .canvas {
    position: relative;
    width: 1200px;
    height: 798px;
  }
  .card {
    position: absolute;
    width: 525px;
    height: 300px;
    border-radius: 4px;
    overflow: hidden;
    box-shadow: 0 6px 18px rgba(40, 20, 60, 0.18);
  }

  /* Front */
  .card--front {
    left: 50px;
    top: 150px;
    background: linear-gradient(160deg, var(--violet-deep) 0%, var(--violet) 45%, var(--violet-light) 70%, var(--violet) 100%);
    color: var(--white);
  }
  .front__brand {
    position: absolute;
    top: 62px;
    left: 0;
    width: 100%;
    display: flex;
    align-items: center;
    justify-content: center;
    gap: 12px;
  }
  .brand-dot {
    width: 12px;
    height: 12px;
    border-radius: 50%;
    background: var(--white);
    flex: none;
  }
  .brand-name {
    font-family: "Josefin Sans", sans-serif;
    font-weight: 400;
    font-size: 30px;
    letter-spacing: 2px;
    text-transform: uppercase;
    line-height: 1;
    white-space: nowrap;
  }
  .front__person {
    position: absolute;
    top: 118px;
    width: 100%;
    text-align: center;
    font-family: "Questrial", sans-serif;
  }
  .person-name { font-size: 29px; line-height: 1.1; }
  .person-role { font-size: 18px; margin-top: 2px; }
  .band {
    position: absolute;
    left: 0;
    bottom: 0;
    width: 100%;
    height: 66px;
    background: var(--band);
    border-top: 5px solid var(--rule);
    display: flex;
    align-items: center;
    color: var(--white);
  }
  .tagline {
    width: 100%;
    text-align: center;
    font-family: "Josefin Sans", sans-serif;
    font-weight: 600;
    font-size: 19px;
    letter-spacing: 2.5px;
    text-transform: uppercase;
    padding-top: 4px;
    white-space: nowrap;
  }

  /* Back */
  .card--back {
    left: 625px;
    top: 340px;
    background: linear-gradient(180deg, var(--lavender) 0%, #d6c8e8 55%, var(--lavender-pale) 100%);
  }
  .geode {
    position: absolute;
    top: -30px;
    left: 215px;
    width: 340px;
    height: 230px;
    border-radius: 50%;
    background: radial-gradient(ellipse at 45% 50%, #b79bd4 0%, #cdbde0 28%, #ece8ef 48%, #d9d2e0 66%, rgba(201, 184, 224, 0) 74%);
  }
  .back__brand {
    position: absolute;
    top: 40px;
    left: 36px;
    display: flex;
    align-items: center;
    gap: 12px;
    color: var(--ink-violet);
  }
  .back__brand .brand-dot { background: var(--ink-violet); }
  .back__brand .brand-name { font-size: 32px; }
  .offer {
    position: absolute;
    top: 96px;
    left: 36px;
    width: 450px;
    font-family: "Questrial", sans-serif;
    font-size: 15px;
    line-height: 1.35;
    color: var(--ink-violet);
  }
  .contact-line {
    position: absolute;
    top: 190px;
    left: 36px;
    right: 30px;
    display: flex;
    justify-content: space-between;
    gap: 16px;
    font-family: "Questrial", sans-serif;
    font-size: 16px;
    color: var(--text-dark);
    white-space: nowrap;
  }
  .phone {
    font-family: "Questrial", sans-serif;
    font-size: 19px;
    letter-spacing: 1px;
    padding-left: 36px;
    white-space: nowrap;
  }
</style>
</head>
<body>
<main class="canvas">

  <section class="card card--front" aria-label="Business card front">
    <div class="front__brand">
      <span class="brand-dot" aria-hidden="true"></span>
      <span class="brand-name">Wildmoss Gems</span>
    </div>
    <div class="front__person">
      <p class="person-name">Marla Kovenberg</p>
      <p class="person-role">Director</p>
    </div>
    <div class="band">
      <p class="tagline">Experience Peace &amp; Serenity</p>
    </div>
  </section>

  <section class="card card--back" aria-label="Business card back">
    <div class="geode" role="img" aria-label="Photograph of an amethyst geode slice"></div>
    <div class="back__brand">
      <span class="brand-dot" aria-hidden="true"></span>
      <span class="brand-name">Wildmoss Gems</span>
    </div>
    <p class="offer">Receive 9 treatments from our qualified practioners and receive a bonus 50% off over $250 crystals, gems and minerals. Conditions apply.</p>
    <div class="contact-line">
      <span class="address">482 Linden Road, Elmridge, Victoria, 3152</span>
      <span class="website">wildmossgems.com.au</span>
    </div>
    <div class="band">
      <p class="phone">1300 519 362</p>
    </div>
  </section>

</main>
</body>
</html>
```